Tamarack Hearth Partners Business Card

Looking for a new business card layout. We are a real estate firm w/ a logo, old design attached. Must keep the same elements on there, just need a fresh look and possible some foil accents. Looking for a simpler design w/ more modern style.

Target Market(s)

Real Estate clients

Industry/Entity Type

Real Estate Agent

Contact Information for Business Card

see attached

Font styles to use
Sans Serif

Requirements
Must have
• all elements on current biz card
Nice to have
• modern look, simpler than we have!
Should not have
• no serif fonts

```html
<!DOCTYPE html>
<html lang="en">
<head>
<meta charset="utf-8">
<title>Tamarack Hearth Partners Business Card</title>
<link href="https://fonts.googleapis.com/css2?family=Exo+2:wght@400;500;700;800&display=swap" rel="stylesheet">
<style>
  :root {
    --backdrop: #1f1f21;
    --card: #050505;
    --edge: #29a9e1;
    --accent-blue: #2ba8e0;
    --divider: #c8262a;
    --ink: #ffffff;
    --ink-soft: #e8e8e8;
    --photo-top: #d9cfc0;
    --photo-bottom: #3bb6c4;
  }
  * { box-sizing: border-box; margin: 0; padding: 0; }
  html, body {
    width: 1200px; height: 900px; overflow: hidden;
    background: var(--backdrop);
    font-family: "Exo 2", sans-serif;
    color: var(--ink);
  }
  .sheet {
    width: 1200px; height: 900px;
    display: flex; flex-direction: column;
    align-items: center; justify-content: center; gap: 30px;
  }
  .card {
    position: relative;
    width: 630px; height: 360px;
    background: var(--card);
    border-left: 4px solid var(--edge);
    border-bottom: 4px solid var(--edge);
  }
  /* Front */
  .card--front { display: flex; align-items: center; justify-content: center; }
  .brand-lockup { display: flex; align-items: center; gap: 14px; }
  .brand-mark { width: 18px; height: 18px; background: var(--ink); }
  .brand-name {
    font-weight: 700; font-size: 34px; letter-spacing: 1px;
    text-transform: uppercase; color: var(--ink);
  }
  /* Back */
  .photo {
    position: absolute; left: 60px; top: 48px;
    width: 150px; height: 190px;
    background: linear-gradient(180deg, var(--photo-top) 0%, #c9b79a 45%, var(--photo-bottom) 100%);
  }
  .agent { position: absolute; left: 40px; top: 244px; width: 190px; text-align: center; }
  .agent-name {
    color: var(--accent-blue); font-weight: 700; font-size: 30px;
    letter-spacing: -1.5px; text-transform: uppercase; line-height: 1;
  }
  .agent-title { font-size: 17px; text-transform: uppercase; letter-spacing: -0.5px; margin-top: 4px; }
  .divider { position: absolute; left: 244px; top: 48px; width: 2px; height: 262px; background: var(--divider); }
  .firm {
    position: absolute; left: 272px; top: 52px; width: 330px;
    font-weight: 800; font-size: 30px; line-height: 1.05;
    text-transform: uppercase; color: var(--ink);
  }
  .contacts { position: absolute; left: 262px; top: 150px; list-style: none; }
  .contacts li {
    display: flex; align-items: center; gap: 12px;
    font-size: 18px; line-height: 27px; color: var(--ink-soft);
  }
  .contacts svg { width: 17px; height: 17px; flex: none; }
  .address { position: absolute; left: 262px; top: 282px; font-size: 18px; color: var(--ink-soft); }
</style>
</head>
<body>
<main class="sheet">
  <section class="card card--front" aria-label="Card front">
    <div class="brand-lockup">
      <span class="brand-mark"></span>
      <span class="brand-name">Tamarack Hearth Partners</span>
    </div>
  </section>

  <section class="card card--back" aria-label="Card back">
    <div class="photo" role="img" aria-label="Portrait photo of the broker"></div>
    <div class="agent">
      <p class="agent-name">Dana Whitfield</p>
      <p class="agent-title">Principal Broker</p>
    </div>
    <div class="divider"></div>
    <p class="firm">Tamarack Hearth Partners</p>
    <ul class="contacts">
      <li>
        <svg viewBox="0 0 24 24" fill="none" stroke="#29a9e1" stroke-width="2"><circle cx="12" cy="12" r="10"/><path d="M8 7l2 0 1 3-1.5 1a7 7 0 0 0 3.5 3.5l1-1.5 3 1 0 2a1.5 1.5 0 0 1-1.5 1.5A9 9 0 0 1 6.5 8.5 1.5 1.5 0 0 1 8 7z"/></svg>
        555.204.7181
      </li>
      <li>
        <svg viewBox="0 0 24 24" fill="none" stroke="#29a9e1" stroke-width="2"><rect x="7" y="2" width="10" height="20" rx="2"/><line x1="11" y1="18" x2="13" y2="18"/></svg>
        555.318.6092
      </li>
      <li>
        <svg viewBox="0 0 24 24" fill="none" stroke="#29a9e1" stroke-width="2"><rect x="2" y="5" width="20" height="14" rx="1"/><path d="M2 6l10 7 10-7"/></svg>
        dana@tamarackhearth.com
      </li>
      <li>
        <svg viewBox="0 0 24 24" fill="none" stroke="#29a9e1" stroke-width="2"><circle cx="12" cy="12" r="10"/><ellipse cx="12" cy="12" rx="4" ry="10"/><line x1="2" y1="12" x2="22" y2="12"/></svg>
        tamarackhearth-homes.com
      </li>
    </ul>
    <p class="address">48 Alder Row, Pinecrest, OR 97000</p>
  </section>
</main>
</body>
</html>
```